Poster Design Project

Poster with modern feeling to be displayed in office. The text that needs to be included in this poster is below:

Rules
1. If it’s not in writing it doesn’t exist.
2. No such thing as 'off the record.'
3. Do not hold a private conversation in a public place.
4. Don’t believe any number that ends in zero.
5. Never turn down an opportunity to eat or go to the bathroom.
6. Don’t spend any of your own money. Don’t even admit you own a credit card. Don’t spend money that is not yours.
7. Not always a 'right' or 'wrong' answer - 'It depends.'
8. In a campaign, someone has to be in charge – campaigns are a place to foster democracy, not practice it.
9. Assume nothing.
10. If you make a mistake, fix it before analyzing. Bad news doesn’t age well.

Industry/Entity Type

Credit Card

Requirements
Must have
• Rules
7. Not always a “right” or “wrong” answer - 'It depends.' 
9. Assume nothing.

```html
<!DOCTYPE html>
<html lang="en">
<head>
<meta charset="utf-8">
<title>Rules</title>
<link href="https://fonts.googleapis.com/css2?family=Cinzel:wght@600;700&family=Cormorant+Garamond:wght@600&display=swap" rel="stylesheet">
<style>
  :root {
    --olive-deep: #5f6318;
    --olive-mid: #8a8a26;
    --olive-light: #a9a33a;
    --band-light: rgba(236, 226, 140, 0.16);
    --band-dark: rgba(40, 42, 6, 0.14);
    --title-cream: #efeadb;
    --text-white: #ffffff;
    --shadow-ink: #1a1608;
    --dot-ink: #2b2010;
  }
  html, body {
    margin: 0;
    padding: 0;
    overflow: hidden;
    background: #6d6e20;
  }
  .poster {
    position: relative;
    width: 810px;
    height: 1200px;
    overflow: hidden;
    background: var(--olive-mid);
  }
  .poster-backdrop {
    position: absolute;
    inset: 0;
    background:
      radial-gradient(ellipse at 18% 8%, rgba(190, 184, 80, 0.55), transparent 45%),
      radial-gradient(ellipse at 70% 55%, rgba(176, 110, 30, 0.28), transparent 55%),
      radial-gradient(ellipse at 20% 90%, rgba(150, 170, 50, 0.35), transparent 50%),
      linear-gradient(170deg, var(--olive-light) 0%, var(--olive-mid) 40%, var(--olive-deep) 100%);
  }
  .band {
    position: absolute;
    left: 0;
    width: 810px;
  }
  .band--top { top: 0; height: 148px; background: var(--band-dark); }
  .band--one { top: 236px; height: 228px; background: var(--band-light); }
  .band--two { top: 478px; height: 236px; background: var(--band-dark); }
  .band--three { top: 714px; height: 258px; background: var(--band-light); }
  .band--four { top: 972px; height: 228px; background: var(--band-dark); }
  .title {
    position: absolute;
    top: 28px;
    left: 0;
    width: 810px;
    margin: 0;
    text-align: center;
    font-family: "Cormorant Garamond", "Times New Roman", serif;
    font-weight: 600;
    font-size: 92px;
    line-height: 1;
    letter-spacing: 1px;
    color: var(--title-cream);
    text-shadow: 4px 4px 0 var(--shadow-ink);
  }
  .dot-rule {
    position: absolute;
    left: 100px;
    width: 626px;
    height: 12px;
    background:
      radial-gradient(circle, var(--dot-ink) 2.6px, transparent 3px) 0 0 / 9px 7px repeat-x,
      radial-gradient(circle, var(--dot-ink) 2px, transparent 2.4px) 4.5px 5px / 9px 7px repeat-x;
  }
  .dot-rule--top { top: 126px; }
  .dot-rule--bottom { top: 1134px; }
  .rule-list {
    position: absolute;
    top: 158px;
    left: 0;
    width: 810px;
    margin: 0;
    padding: 0;
    list-style: none;
    text-align: center;
    font-family: "Cinzel", "Copperplate", serif;
    font-weight: 700;
    font-size: 27px;
    line-height: 40.7px;
    color: var(--text-white);
    text-shadow: 2px 2px 0 var(--shadow-ink);
    letter-spacing: 0.3px;
  }
  .rule-line { display: block; white-space: nowrap; }
</style>
</head>
<body>
<main class="poster">
  <div class="poster-backdrop" role="img" aria-label="Abstract olive green backdrop with sweeping orange and yellow curved lines"></div>
  <div class="band band--top"></div>
  <div class="band band--one"></div>
  <div class="band band--two"></div>
  <div class="band band--three"></div>
  <div class="band band--four"></div>

  <h1 class="title">RULES</h1>
  <div class="dot-rule dot-rule--top"></div>

  <ol class="rule-list">
    <li>
      <span class="rule-line">1. If it’s not in writing it doesn’t</span>
      <span class="rule-line">exist.</span>
    </li>
    <li>
      <span class="rule-line">2. No such thing as 'off the record.'</span>
    </li>
    <li>
      <span class="rule-line">3. Do not hold a private</span>
      <span class="rule-line">conversation in a public place.</span>
    </li>
    <li>
      <span class="rule-line">4. Don’t believe any number that</span>
      <span class="rule-line">ends in zero.</span>
    </li>
    <li>
      <span class="rule-line">5. Never turn down an opportunity</span>
      <span class="rule-line">to eat or go to the bathroom.</span>
    </li>
    <li>
      <span class="rule-line">6. Don’t spend any of your own</span>
      <span class="rule-line">money. Don’t even admit you own a</span>
      <span class="rule-line">credit card. Don’t spend money that</span>
      <span class="rule-line">is not yours.</span>
    </li>
    <li>
      <span class="rule-line">7. Not always a 'right' or 'wrong'</span>
      <span class="rule-line">answer – 'It depends.'</span>
    </li>
    <li>
      <span class="rule-line">8. In a campaign, someone has to be</span>
      <span class="rule-line">in charge – campaigns are a place to</span>
      <span class="rule-line">foster democracy, not practice it.</span>
    </li>
    <li>
      <span class="rule-line">9. Assume nothing.</span>
    </li>
    <li>
      <span class="rule-line">10. If you make a mistake, fix it</span>
      <span class="rule-line">before analyzing. Bad news doesn’t</span>
      <span class="rule-line">age well.</span>
    </li>
  </ol>

  <div class="dot-rule dot-rule--bottom"></div>
</main>
</body>
</html>
```